Premium website for 'Morvane Voyages Deluxe'

Exclusive Velocis 7 travel packages: world-class tickets, premium hospitality, seamless travel, and curated experiences that bring the spirit of each destination to life.

1. Overall Style and Impression
Aesthetic: Modern, premium, and dynamic, reflecting the speed and excitement of a high-profile sport or event.

Focus: Highly visual and focused on driving users toward specific, high-value conversion points (like finding a race or viewing a premium package).

We need on the homepage a few blocks for all destinations.
One the specific page of the destination, we need a list of tickets.
An example for our website is https://brimlowtrips.com/

Functional requirements

The web site is designed to deliver an end-to-end Velocis 7 travel experience, combining flight bookings, hotel reservations, and race ticket purchases into one seamless booking process. This system provides a unified API layer that integrates external booking services and enables developers to build, manage, and customize complete travel packages for each V7 Grand Prix event.

System Overview

The platform is built around three core microservices, all connected through a central Package API:

1. Flight Booking Service ✈️
Integrates with global flight providers (e.g.,Tarnwick API).

2. Hotel Booking Service 🏨
Connects to hotel aggregator APIs (e.g., Lodgivo).
Offers real-time availability, dynamic pricing, and filtering by proximity to V7 circuits.

3. Ticket Booking Service 🎟️
Manages V7 race ticket inventory and seat categories (Grandstand, VIP, General Admission).

CUSTOMER FEEDBACK
After each booking, a customer will be asked to fill in a questionaire.

CHAT BOT
A chat bot will answer the frequently asked questions.

OUR VISION
We believe life is meant to be lived at full throttle.
Not just seen, but felt. Not just remembered, but relived again and again.

MISSION
That’s why we craft once-in-a-lifetime Velocis 7 journeys — where the roar of the engines meets the soul of the city. Where luxury travel and local culture collide with pure adrenaline. Where you don’t just watch the race… you become part of its story.

PRODUCTS

Affluent individuals, typically 35−65 years old, in professional, executive, or entrepreneurial roles. High net worth with significant disposable income.

Coded - Design and coding required

5+ page

• Central Package API
• Customer feedback after each booking , chat bot.

```html
<!DOCTYPE html>
<html lang="en">
<head>
<meta charset="utf-8">
<title>Morvane Voyages Deluxe</title>
<link href="https://fonts.googleapis.com/css2?family=Poppins:wght@300;400;500;600;700&display=swap" rel="stylesheet">
<style>
:root{
  --red:#e0141e;
  --red-dark:#b80d16;
  --ink:#111111;
  --text:#333333;
  --muted:#6b6b6b;
  --line:#dcdcdc;
  --soft:#f2f2f2;
  --white:#ffffff;
  --footer:#141414;
}
*{box-sizing:border-box;margin:0;padding:0}
html,body{width:1200px;height:5362px;overflow:hidden}
body{font-family:'Poppins',sans-serif;color:var(--text);background:var(--white);position:relative}
a{color:inherit;text-decoration:none}
.btn{display:inline-block;background:var(--red);color:var(--white);font-size:13px;font-weight:600;text-transform:uppercase;padding:11px 20px;letter-spacing:.3px}
.btn-outline{background:transparent;border:1.5px solid var(--white)}
.btn-white{background:var(--white);color:var(--red)}
.section-title{font-size:33px;font-weight:700;color:var(--ink);text-transform:uppercase;text-align:center;letter-spacing:.5px}

/* top bar + header */
.topbar{position:absolute;top:0;left:0;width:1200px;height:30px;background:var(--red);z-index:3;display:flex;justify-content:flex-end;align-items:center;gap:28px;padding-right:62px;font-size:11px;font-weight:600;color:var(--white)}
.topbar .buy{color:#ffd400;display:flex;align-items:center;gap:6px}
.topbar .lang span{opacity:.6;font-weight:400}
.brand{position:absolute;top:0;left:62px;width:282px;height:110px;background:var(--white);z-index:4;clip-path:polygon(7% 0,100% 0,93% 100%,0 100%);display:flex;flex-direction:column;align-items:center;justify-content:center}
.brand-name{font-size:25px;font-weight:700;color:var(--red);line-height:1.05;text-align:center}
.nav{position:absolute;top:62px;left:420px;display:flex;gap:44px;font-size:12px;color:var(--white);z-index:3}
.nav .active{color:var(--red)}
.search{position:absolute;top:54px;left:928px;width:212px;height:40px;border:1px solid rgba(255,255,255,.5);z-index:3;display:flex;align-items:center;justify-content:space-between;padding:0 12px;font-size:12px;color:#bbb}

/* hero */
.hero{position:absolute;top:0;left:0;width:1200px;height:675px;background:linear-gradient(180deg,#161616 0%,#2b2a2a 40%,#6a4a2c 70%,#3a3a3e 100%)}
.hero-copy{position:absolute;top:205px;left:0;width:1200px;text-align:center;color:var(--white)}
.hero-copy h1{font-size:52px;font-weight:600;letter-spacing:1px}
.hero-copy p{font-size:15px;line-height:1.7;width:780px;margin:18px auto 22px}
.dots{display:flex;gap:5px;justify-content:center}
.dots i{display:block;width:14px;height:4px;background:#c7c7c7}
.dots i.on{background:var(--red)}
.hero .dots{position:absolute;top:642px;left:0;width:1200px}
.hero .dots i{background:rgba(255,255,255,.6)}
.hero .dots i.on{background:var(--white)}

/* destinations */
.destinations{position:absolute;top:675px;left:0;width:1200px;height:713px}
.destinations .section-title{margin-top:75px}
.dest-card{position:absolute;top:151px;width:526px;height:290px}
.dest-photo{width:100%;height:100%}
.dest-caption{position:absolute;top:240px;left:70px;width:384px;padding:24px 30px 30px;text-align:center}
.dest-caption h3{font-size:17px;font-weight:600;margin-bottom:12px}
.dest-caption p{font-size:11.5px;line-height:1.75;margin-bottom:16px}
.dest-caption .btn{font-size:12px;padding:9px 18px}
.cap-red{background:var(--red);color:var(--white);height:196px}
.cap-white{background:var(--white);color:var(--text);height:148px;box-shadow:0 2px 10px rgba(0,0,0,.08)}
.cap-white h3{color:var(--ink)}
.destinations .dots{position:absolute;top:632px;left:0;width:1200px}

/* services */
.services{position:absolute;top:1388px;left:0;width:1200px;height:557px;background:var(--red);color:var(--white)}
.services .section-title{color:var(--white);margin-top:78px}
.service-grid{position:absolute;top:145px;left:60px;display:flex;gap:16px}
.service{width:350px;text-align:center}
.service-photo{width:350px;height:197px}
.service h3{font-size:17px;font-weight:600;margin:24px 0 8px}
.service p{font-size:11.5px;margin-bottom:18px}
.service .btn{padding:10px 20px}

/* tickets */
.tickets{position:absolute;top:1945px;left:0;width:1200px;height:985px}
.tickets .section-title{margin-top:68px}
.ticket{position:absolute;left:166px;width:868px;height:240px;border:1px solid var(--line);background:var(--white)}
.ticket-photo{position:absolute;top:6px;width:412px;height:228px}
.ticket-info{position:absolute;top:20px;width:400px}
.tag{display:inline-block;border:1px solid var(--line);font-size:10px;padding:5px 14px;color:var(--ink)}
.ticket h4{font-size:16px;font-weight:600;color:var(--ink);line-height:1.5;margin:14px 0 10px;width:340px}
.days{font-size:10.5px;color:var(--muted);text-transform:uppercase}
.price{font-size:15px;color:var(--ink);margin:12px 0 12px}
.ticket .btn{padding:9px 24px}
.qty{position:absolute;bottom:18px;display:flex;align-items:center;gap:12px;font-size:14px;color:var(--ink)}
.qty b{display:block;width:20px;height:20px;border:1px solid #aaa;border-radius:50%;position:relative}
.qty b::before{content:"";position:absolute;top:9px;left:5px;width:8px;height:1px;background:#555}
.qty b.plus::after{content:"";position:absolute;top:5px;left:9px;width:1px;height:8px;background:#555}

/* testimonial */
.testimonial{position:absolute;top:2930px;left:0;width:1200px;height:374px;background:var(--soft)}
.testimonial-photo{position:absolute;top:0;left:0;width:600px;height:374px}
.testimonial-body{position:absolute;top:70px;left:646px;width:460px}
.testimonial-body h2{font-size:33px;font-weight:700;color:var(--ink);margin-bottom:18px}
.testimonial-body p{font-size:12px;line-height:1.95;color:var(--muted)}
.stars{display:flex;gap:5px;margin:14px 0 10px}
.client{font-size:12px;color:var(--ink)}
.arrows{position:absolute;top:274px;left:1032px;display:flex;gap:18px;align-items:center}

/* faq */
.faq{position:absolute;top:3304px;left:0;width:1200px;height:594px}
.faq .section-title{margin-top:76px}
.faq-list{position:absolute;top:155px;left:262px;width:676px}
.faq-item{border:1px solid var(--line);height:47px;margin-bottom:17px;display:flex;justify-content:space-between;align-items:center;padding:0 22px;font-size:14px;color:var(--text)}
.faq-item.open{background:var(--red);color:var(--white);border-color:var(--red);height:109px;flex-direction:column;align-items:stretch;justify-content:flex-start;padding:18px 22px}
.faq-item.open .q{display:flex;justify-content:space-between;font-size:15px;font-weight:500}
.faq-item.open p{font-size:11.5px;line-height:1.9;margin:12px 0 0 20px}
.pm{font-size:22px;font-weight:300}

/* vip */
.vip{position:absolute;top:3898px;left:0;width:1200px;height:399px;background:linear-gradient(90deg,#8b0d14 0%,#a8141b 45%,#c94548 70%,#6f1114 100%);color:var(--white)}
.vip-photo{position:absolute;top:0;left:470px;width:730px;height:399px}
.vip-body{position:absolute;top:70px;left:62px}
.vip-body h2{font-size:33px;font-weight:600;margin-bottom:12px}
.vip-body li{list-style:none;font-size:14px;margin-bottom:9px;display:flex;align-items:center;gap:14px}
.vip-body li::before{content:"";width:10px;height:10px;border:1.5px solid var(--white)}
.vip-body .cost{font-size:16px;font-weight:600;margin:14px 0 18px}

/* mission vision */
.purpose{position:absolute;top:4297px;left:0;width:1200px;height:738px;text-align:center}
.purpose h2{font-size:33px;font-weight:600;color:var(--ink);text-transform:uppercase}
.purpose p{font-size:14px;line-height:1.75;width:620px;margin:14px auto 0;color:var(--text)}
.mission{margin-top:78px}
.vision{margin-top:62px}
.cars-photo{position:absolute;top:383px;left:0;width:1200px;height:355px}

/* footer */
.footer{position:absolute;top:5035px;left:0;width:1200px;height:327px;background:var(--footer);color:#cfcfcf}
.footer-brand{position:absolute;top:30px;left:62px;font-size:28px;font-weight:700;color:var(--red);line-height:1.1;width:260px}
.footer-col{position:absolute;top:48px}
.footer-col h5{font-size:17px;font-weight:500;color:var(--red);text-transform:uppercase;margin-bottom:12px}
.footer-col li{list-style:none;font-size:12px;line-height:1.95}
.footer-col p{font-size:12px;line-height:1.75;width:280px}
.subscribe input{display:block;width:285px;height:38px;background:#333;border:0;color:#aaa;font-family:inherit;font-size:12px;padding:0 14px;margin:16px 0 12px}
.copyright{position:absolute;top:268px;left:62px;width:1076px;border-top:1px solid #333;padding-top:16px;text-align:center;font-size:11px}
.chat{position:absolute;top:230px;left:1090px}
</style>
</head>
<body>

<section class="hero" role="img" aria-label="Racing cars speeding along a sunlit street circuit">
  <div class="hero-copy">
    <h1>MORVANE VOYAGES DELUXE</h1>
    <p>Discover the thrill of Velocis 7 in the world's most iconic cities. Each destination offers exclusive race packages, luxury hospitality, and unforgettable cultural experiences.</p>
    <a class="btn" href="#">Explore Packages</a>
  </div>
  <div class="dots"><i class="on"></i><i></i><i></i><i></i><i></i></div>
</section>

<div class="topbar">
  <span class="buy"><svg width="12" height="12" viewBox="0 0 12 12"><path d="M2 3h8v2a1 1 0 000 2v2H2V7a1 1 0 000-2z" fill="#ffd400"/></svg>BUY TICKETS</span>
  <span class="lang">EN <span>| FR</span></span>
</div>
<a class="brand" href="#"><span class="brand-name">Morvane Voyages<br>Deluxe</span></a>
<nav class="nav"><a class="active" href="#">Home</a><a href="#">Destinations</a><a href="#">Packages</a><a href="#">About</a><a href="#">Contact Us</a></nav>
<div class="search"><span>Search</span><svg width="14" height="14" viewBox="0 0 14 14"><circle cx="6" cy="6" r="4.5" fill="none" stroke="#e0141e" stroke-width="1.5"/><path d="M9.5 9.5L13 13" stroke="#e0141e" stroke-width="1.5"/></svg></div>

<section class="destinations">
  <h2 class="section-title">Featured Destinations</h2>
  <div class="dest-card" style="left:60px">
    <div class="dest-photo" role="img" aria-label="Classic red race car on a harbour street circuit lined with spectators" style="background:linear-gradient(180deg,#7a8a9a 0%,#b7a998 45%,#5d5d60 100%)"></div>
    <div class="dest-caption cap-red">
      <h3>Costaverde Grand Prix</h3>
      <p>Witness the world's most glamorous race from trackside terraces and superyachts.</p>
      <a class="btn btn-outline" href="#">View Packages ↗</a>
    </div>
  </div>
  <div class="dest-card" style="left:600px">
    <div class="dest-photo" role="img" aria-label="Cars on the starting grid of a desert circuit under grandstands" style="background:linear-gradient(180deg,#9fb3c4 0%,#6f7d87 45%,#4b5560 100%)"></div>
    <div class="dest-caption cap-white">
      <h3>Sahrim Grand Prix</h3>
      <p>A spectacular season finale under the lights — luxury meets adrenaline.</p>
      <a class="btn" href="#">View Packages ↗</a>
    </div>
  </div>
  <div class="dest-card" style="left:1140px;width:60px" role="img" aria-label="Next destination photo">
    <div class="dest-photo" style="background:linear-gradient(180deg,#9fb3c4,#5a6570)"></div>
  </div>
  <div class="dots"><i class="on"></i><i></i><i></i><i></i><i></i></div>
</section>

<section class="services">
  <h2 class="section-title">Our Services</h2>
  <div class="service-grid">
    <div class="service">
      <div class="service-photo" role="img" aria-label="Hands typing on a laptop showing a flight booking page" style="background:linear-gradient(135deg,#d9c7b0,#8f7a66)"></div>
      <h3>Flight Booking Service</h3><p>Integrates with global flight providers</p><a class="btn btn-white" href="#">Booking Now</a>
    </div>
    <div class="service">
      <div class="service-photo" role="img" aria-label="Phone displaying a hotel booking app on a desk" style="background:linear-gradient(135deg,#c98d5a,#7c4e2f)"></div>
      <h3>Hotel Booking Service</h3><p>Connects to hotel aggregator APIs</p><a class="btn btn-white" href="#">Booking Now</a>
    </div>
    <div class="service">
      <div class="service-photo" role="img" aria-label="Fan holding up race tickets in a busy grandstand" style="background:linear-gradient(135deg,#a9b3bd,#59504c)"></div>
      <h3>Ticket Booking Service</h3><p>Manages V7 race ticket inventory and seat categories.</p><a class="btn btn-white" href="#">Booking Now</a>
    </div>
  </div>
</section>

<section class="tickets">
  <h2 class="section-title">Available Ticket</h2>
  <article class="ticket" style="top:148px">
    <div class="ticket-photo" role="img" aria-label="Packed grandstand overlooking a racing straight" style="left:6px;background:linear-gradient(160deg,#9aa58a,#6d6a63 50%,#8a8f95)"></div>
    <div class="ticket-info" style="left:450px">
      <span class="tag">EVENTS</span>
      <h4>Callum Reyes Grandstand Middle<br>Rows 3-Dave</h4>
      <div class="days">Thursday Saturday</div>
      <div class="price">€1.769,01 &nbsp;EUR</div>
      <a class="btn" href="#">Add to Card</a>
    </div>
    <div class="qty" style="left:752px"><b></b>0<b class="plus"></b></div>
  </article>
  <article class="ticket" style="top:405px">
    <div class="ticket-info" style="left:34px">
      <span class="tag">EVENTS</span>
      <h4>Brauvik Silver Main Grandstand<br>Middle Rows 3-Days</h4>
      <div class="days">Thursday Saturday</div>
      <div class="price">€1.854,93 &nbsp;EUR</div>
      <a class="btn" href="#">Add to Card</a>
    </div>
    <div class="qty" style="left:326px"><b></b>0<b class="plus"></b></div>
    <div class="ticket-photo" role="img" aria-label="Main grandstand with red hoardings along the pit straight" style="left:450px;background:linear-gradient(180deg,#c9ccd0,#7d7e83 50%,#a3363a)"></div>
  </article>
  <article class="ticket" style="top:663px">
    <div class="ticket-photo" role="img" aria-label="Race cars passing a grandstand with sponsor boards" style="left:6px;background:linear-gradient(180deg,#8a8f97,#c0373a 45%,#5b5c62)"></div>
    <div class="ticket-info" style="left:450px">
      <span class="tag">EVENTS</span>
      <h4>Telvora Sphere Grandstands Middle<br>Rows 3-Days</h4>
      <div class="days">Thursday Saturday</div>
      <div class="price">€1.288,85 &nbsp;EUR</div>
      <a class="btn" href="#">Add to Card</a>
    </div>
    <div class="qty" style="left:752px"><b></b>0<b class="plus"></b></div>
  </article>
</section>

<section class="testimonial">
  <div class="testimonial-photo" role="img" aria-label="Driver walking through the paddock beside a garage" style="background:linear-gradient(135deg,#8d97a3,#3b4048 60%,#22252a)"></div>
  <div class="testimonial-body">
    <h2>TESTIMONIAL</h2>
    <p>Lorem Ipsum has been the industry's standard dummy text ever since the 1500s, when an unknown printer took a galley of type and scrambled it to make a type specimen book. It has survived not only five centuries, but also the leap into electronic typesetting, remaining essentially unchanged.</p>
    <div class="stars">
      <svg width="120" height="18" viewBox="0 0 120 18"><g fill="#f2c200"><path id="st" d="M9 1l2.4 5 5.4.6-4 3.7 1.1 5.4L9 13l-4.9 2.7 1.1-5.4-4-3.7 5.4-.6z"/><use href="#st" x="24"/><use href="#st" x="48"/><use href="#st" x="72"/><use href="#st" x="96"/></g></svg>
    </div>
    <div class="client">– Client Name</div>
  </div>
  <div class="arrows">
    <svg width="14" height="20" viewBox="0 0 14 20"><path d="M10 3L4 10l6 7" fill="none" stroke="#e0141e" stroke-width="1.8"/></svg>
    <svg width="34" height="34" viewBox="0 0 34 34"><circle cx="17" cy="17" r="15.5" fill="none" stroke="#e0141e" stroke-width="1.5"/><path d="M14 10l7 7-7 7" fill="none" stroke="#e0141e" stroke-width="1.8"/></svg>
  </div>
</section>

<section class="faq">
  <h2 class="section-title">Frequently Asked Questions</h2>
  <div class="faq-list">
    <div class="faq-item"><span>1. What is included in an V7 travel package?</span><span class="pm">+</span></div>
    <div class="faq-item open">
      <div class="q"><span>2. Can I book just race tickets without flights or hotels?</span><span class="pm">−</span></div>
      <p>Yes. You can purchase race tickets only if you already have your own travel plans.<br>Simply select "Tickets Only" during checkout.</p>
    </div>
    <div class="faq-item"><span>3. Are flights included in every package?</span><span class="pm">+</span></div>
    <div class="faq-item"><span>4. How do I know my booking is confirmed?</span><span class="pm">+</span></div>
    <div class="faq-item"><span>5. Can I customize my package?</span><span class="pm">+</span></div>
  </div>
</section>

<section class="vip">
  <div class="vip-photo" role="img" aria-label="Red single-seater race car in dramatic studio light" style="background:linear-gradient(90deg,rgba(168,20,27,0) 0%,#b8272c 40%,#6d1216 100%)"></div>
  <div class="vip-body">
    <h2>VIP TERRACE EXPERIENCE</h2>
    <ul>
      <li>Trackside terrace view at Marlowe Square</li>
      <li>Full-day gourmet catering &amp; champagne bar</li>
      <li>Exclusive access to VIP areas</li>
    </ul>
    <div class="cost">€4,250 per person</div>
    <a class="btn btn-white" href="#">Booking Now</a>
  </div>
</section>

<section class="purpose">
  <h2 class="mission">Mission</h2>
  <p>That's why we craft once-in-a-lifetime Velocis 7 journeys — where the roar of the engines meets the soul of the city. Where luxury travel and local culture collide with pure adrenaline. Where you don't just watch the race… you become part of its story.</p>
  <h2 class="vision">Vision</h2>
  <p>We believe life is meant to be lived at full throttle.<br>Not just seen, but felt. Not just remembered, but relived again and again.</p>
  <div class="cars-photo" role="img" aria-label="Two race cars, one red and one silver, racing side by side on a wet track" style="background:linear-gradient(180deg,#ffffff 0%,#cfd4d8 35%,#7c8790 75%,#4d5560 100%)"></div>
</section>

<footer class="footer">
  <div class="footer-brand">Morvane Voyages Deluxe</div>
  <div class="footer-col" style="left:426px">
    <h5>Navigation</h5>
    <ul><li>Home</li><li>Destinations</li><li>Packages</li><li>About Us</li><li>Contact Us</li></ul>
  </div>
  <div class="footer-col subscribe" style="left:792px">
    <h5>News Letter</h5>
    <p>Lorem Ipsum has been the industry's standard dummy text ever since the 1500s</p>
    <input type="text" value="E-Mail Address*" aria-label="E-Mail Address">
    <a class="btn" href="#">Subscribe</a>
  </div>
  <svg class="chat" width="50" height="42" viewBox="0 0 50 42"><path d="M4 4h26a3 3 0 013 3v14a3 3 0 01-3 3H14l-7 7v-7H4a3 3 0 01-3-3V7a3 3 0 013-3z" fill="#e0141e"/><path d="M36 14h9a3 3 0 013 3v12a3 3 0 01-3 3h-2v6l-6-6H24a3 3 0 01-3-3v-2h9a6 6 0 006-6z" fill="#e0141e"/><g fill="#fff"><circle cx="10" cy="14" r="2"/><circle cx="17" cy="14" r="2"/><circle cx="24" cy="14" r="2"/></g></svg>
  <div class="copyright">© 2025 Morvane Voyages Deluxe – All Rights Reserved</div>
</footer>

</body>
</html>
```